Property Maintenance company needs a noticeable Car Wrap design

We need an outstanding car wrap design for our Corvane Tessel Cargolite 2020. It needs to emphasize that our property maintenance company serves both Commercial and Residential clients. The wrap should communicate friendliness and quality services. I have attached a pdf file that outlines all the requirements for the wrap design. I also attached all relevant pictures to help with the creation of the design. The selected winner will receive the source files of the company logo & QTR logo to use in the car wrap design. I look forward to seeing all your designs!

Thank you!

Target Market(s)

Property Maintenance
Residential homeowners
Building owners

Industry/Entity Type

Property Maintenance

Requirements
Must have
• See Instruction file for all details.
Nice to have
• Some small icons that represent electrical, plumbing, handyman, and carpentry work.
For example, like a lightbulb, plug, or pipe icon. Or all of them. Try to use intuitive icons so the general public will know what it is.

Thanks!

```html
<!DOCTYPE html>
<html lang="en">
<head>
<meta charset="utf-8">
<title>Brightkeep Maintenance Services – Van Wrap</title>
<link rel="stylesheet" href="https://fonts.googleapis.com/css2?family=Poppins:wght@400;500;700&family=Oswald:wght@600&display=swap">
<style>
  :root {
    --brand-blue: #4a7fe0;
    --brand-navy: #0f2a78;
    --brand-green: #6fbe3a;
    --body-white: #ffffff;
    --trim-black: #1d1f22;
    --glass: #9ea3a8;
    --rim: #c9ccd0;
    --panel-line: #c4c7cc;
    --page: #ffffff;
  }
  html, body { margin: 0; padding: 0; overflow: hidden; background: var(--page); }
  .canvas { width: 1200px; height: 1200px; display: block; }
  .van-body { fill: var(--body-white); stroke: var(--panel-line); stroke-width: 1.5; }
  .van-glass { fill: var(--glass); }
  .trim { fill: var(--trim-black); }
  .tyre { fill: var(--trim-black); }
  .rim { fill: var(--rim); stroke: #9a9ea3; stroke-width: 2; }
  .panel-line { stroke: var(--panel-line); stroke-width: 1.5; fill: none; }
  .handle { fill: var(--trim-black); }
  .band-blue { fill: var(--brand-blue); }
  .band-green { fill: var(--brand-green); }
  .band-navy { fill: var(--brand-navy); }
  .brand-name { font-family: "Poppins", sans-serif; font-weight: 500; font-size: 40px; fill: var(--brand-navy); letter-spacing: 1px; }
  .brand-sub { font-family: "Poppins", sans-serif; font-weight: 500; font-size: 13.5px; letter-spacing: 5px; fill: var(--brand-blue); }
  .brand-mark { fill: none; stroke: var(--brand-blue); stroke-width: 4; }
  .web { font-family: "Poppins", sans-serif; font-weight: 400; font-size: 14px; }
  .web b { font-weight: 700; }
  .phone { font-family: "Poppins", sans-serif; font-weight: 700; font-size: 23px; }
  .tagline { font-family: "Oswald", sans-serif; font-weight: 600; font-size: 23px; letter-spacing: 1px; }
  .on-blue { fill: var(--body-white); }
  .on-white-blue { fill: var(--brand-blue); }
  .on-white-navy { fill: var(--brand-navy); }
  .on-green { fill: var(--body-white); }
  .service-ring { fill: none; stroke: var(--body-white); stroke-width: 2; }
  .service-disc { fill: var(--brand-navy); stroke: var(--body-white); stroke-width: 3; }
  .service-icon { fill: none; stroke: var(--body-white); stroke-width: 3.5; stroke-linecap: round; stroke-linejoin: round; }
  .service-label { font-family: "Poppins", sans-serif; font-weight: 700; font-size: 5px; fill: var(--body-white); text-anchor: middle; }
  .service-label-green { font-family: "Poppins", sans-serif; font-weight: 700; font-size: 5.5px; fill: var(--brand-green); text-anchor: middle; }
  .rating-badge { fill: var(--brand-navy); }
</style>
</head>
<body>
<svg class="canvas" viewBox="0 0 960 960" xmlns="http://www.w3.org/2000/svg">
  <defs>
    <path id="van-outline" d="M36,300 Q42,258 110,238 L240,200 Q300,122 380,96 Q600,78 884,78 Q906,82 914,130 L926,300 L928,368 Q928,388 905,388 L868,388 A64,64 0 0 0 740,388 L246,388 A64,64 0 0 0 118,388 L58,388 Q36,384 34,346 Z"/>
    <clipPath id="van-clip"><use href="#van-outline"/></clipPath>

    <symbol id="icon-carpentry" viewBox="-20 -20 40 40">
      <path class="service-icon" d="M-12,-12 L12,12 M10,-13 L-12,9 M12,-8 L6,-14 M-14,7 L-8,13"/>
    </symbol>
    <symbol id="icon-handyman" viewBox="-20 -20 40 40">
      <path class="service-icon" d="M-12,12 L6,-6 M0,-14 L10,-4 L14,-8 L4,-16 Z M12,12 L-6,-6 M-12,-10 L-8,-14"/>
    </symbol>
    <symbol id="icon-plumbing" viewBox="-20 -20 40 40">
      <path class="service-icon" d="M-10,-14 L-10,2 Q-10,12 0,12 Q10,12 10,2 L10,-2 M6,-2 L14,-2 M-14,-14 L-6,-14"/>
    </symbol>
    <symbol id="icon-electrical" viewBox="-20 -20 40 40">
      <path class="service-icon" d="M-9,-6 L9,-6 L9,2 Q9,9 0,9 Q-9,9 -9,2 Z M-4,-6 L-4,-14 M4,-6 L4,-14 M0,9 L0,14 Q0,17 4,17"/>
    </symbol>

    <g id="van-base">
      <use href="#van-outline" class="van-body"/>
      <path class="van-glass" d="M272,124 L466,120 L466,214 L262,218 Q262,160 272,124 Z"/>
      <rect class="trim" x="226" y="188" width="22" height="30" rx="5"/>
    </g>
    <g id="van-detail">
      <path class="panel-line" d="M258,120 L258,380 M488,88 L488,380 M670,82 L670,380"/>
      <rect class="handle" x="456" y="240" width="10" height="26" rx="4"/>
      <rect class="handle" x="492" y="240" width="10" height="26" rx="4"/>
      <rect class="trim" x="296" y="318" width="334" height="12" rx="6"/>
      <path class="trim" d="M34,340 Q36,384 58,388 L118,388 A64,64 0 0 1 246,388 L250,394 L60,398 Q30,396 30,350 Z"/>
      <path class="trim" d="M740,388 A64,64 0 0 1 868,388 L905,388 Q928,388 928,368 L926,300 L934,300 L934,380 Q932,398 905,398 L740,398 Z"/>
      <circle class="tyre" cx="182" cy="388" r="56"/>
      <circle class="rim" cx="182" cy="388" r="36"/>
      <circle class="tyre" cx="804" cy="388" r="56"/>
      <circle class="rim" cx="804" cy="388" r="36"/>
    </g>
  </defs>

  <!-- Van one: blue band layout -->
  <g class="wrap wrap-blue-band">
    <use href="#van-base"/>
    <g clip-path="url(#van-clip)">
      <path class="band-green" d="M60,238 L940,220 L940,230 L60,248 Z"/>
      <path class="band-blue" d="M60,252 L940,234 L940,296 L60,306 Z"/>
    </g>
    <use href="#van-detail"/>

    <g class="brand-lockup">
      <rect class="brand-mark" x="514" y="102" width="30" height="62"/>
      <text class="brand-name" x="554" y="184">BRIGHTKEEP</text>
      <text class="brand-sub" x="518" y="213">MAINTENANCE SERVICES</text>
    </g>

    <rect class="rating-badge" x="172" y="266" width="20" height="28" rx="2"/>

    <text class="web on-blue" x="278" y="271">www.<tspan font-weight="700">brightkeepfs</tspan>.com</text>
    <text class="phone on-blue" x="276" y="294">555-013-2480</text>

    <g class="service-icons">
      <circle class="service-ring" cx="598" cy="266" r="28"/>
      <use href="#icon-carpentry" x="583" y="246" width="30" height="30"/>
      <text class="service-label" x="598" y="285">CARPENTRY WORK</text>
      <circle class="service-ring" cx="668" cy="266" r="28"/>
      <use href="#icon-handyman" x="653" y="246" width="30" height="30"/>
      <text class="service-label" x="668" y="285">HANDYMAN</text>
      <circle class="service-ring" cx="742" cy="266" r="28"/>
      <use href="#icon-plumbing" x="727" y="246" width="30" height="30"/>
      <text class="service-label" x="742" y="285">PLUMBING</text>
      <circle class="service-ring" cx="818" cy="264" r="28"/>
      <use href="#icon-electrical" x="803" y="244" width="30" height="30"/>
      <text class="service-label" x="818" y="283">ELECTRICAL</text>
    </g>

    <text class="tagline on-white-navy" x="312" y="370">PROPERTY MAINTENANCE SERVICES</text>
  </g>

  <!-- Van two: green sweep layout -->
  <g class="wrap wrap-green-sweep" transform="translate(0,450)">
    <use href="#van-base"/>
    <g clip-path="url(#van-clip)">
      <path class="band-green" d="M230,334 Q520,296 700,240 Q820,190 880,70 L940,70 L940,400 L230,400 Z"/>
      <path class="band-blue" d="M230,330 Q400,312 560,290 L560,296 Q400,320 230,338 Z"/>
      <path class="band-blue" d="M600,400 Q770,330 940,258 L940,300 Q800,350 680,400 Z"/>
    </g>
    <use href="#van-detail"/>

    <g class="brand-lockup">
      <rect class="brand-mark" x="502" y="102" width="28" height="56"/>
      <text class="brand-name" x="540" y="160" style="font-size:35px">BRIGHTKEEP</text>
      <text class="brand-sub" x="502" y="186" style="font-size:12px">MAINTENANCE SERVICES</text>
    </g>

    <rect class="rating-badge" x="166" y="252" width="20" height="28" rx="2"/>

    <text class="web on-white-blue" x="276" y="269">www.<tspan font-weight="700" fill="var(--brand-green)">brightkeepfs</tspan>.com</text>
    <text class="phone on-white-navy" x="274" y="297">555-013-2480</text>

    <g class="service-icons">
      <circle class="service-disc" cx="687" cy="266" r="34"/>
      <use href="#icon-carpentry" x="670" y="242" width="34" height="34"/>
      <text class="service-label-green" x="687" y="286">CARPENTRY</text>
      <text class="service-label-green" x="687" y="292">WORK</text>
      <circle class="service-disc" cx="755" cy="230" r="34"/>
      <use href="#icon-handyman" x="738" y="206" width="34" height="34"/>
      <text class="service-label-green" x="755" y="252">HANDYMAN</text>
      <circle class="service-disc" cx="812" cy="180" r="34"/>
      <use href="#icon-plumbing" x="795" y="156" width="34" height="34"/>
      <text class="service-label-green" x="812" y="202">PLUMBING</text>
      <circle class="service-disc" cx="852" cy="112" r="34"/>
      <use href="#icon-electrical" x="835" y="88" width="34" height="34"/>
      <text class="service-label-green" x="852" y="134">ELECTRICAL</text>
    </g>

    <text class="tagline on-green" x="310" y="364">PROPERTY MAINTENANCE SERVICES</text>
  </g>
</svg>
</body>
</html>
```